Website for new child psychology practice

New clinical psychology practice in NSW Australia, specialising in work with children, adolescents and families. I would like to feature the colours in the logo, which was recently designed by pixelhive designer Odette.
I am seeking a professional looking page, which is easy to navigate and is colourful and playful but not childish.
Target Market(s)
Parents and professionals
Industry/Entity Type
Health
Coding
Coded - Design and coding required
Number of Pages Required
1 page
Font styles to use
Serif
Requirements
Must have
- Pages for 'About us' 'Services' 'Fees and information' 'Contact us'
Should not have
- Childish stock photos

```html
<!DOCTYPE html>
<html lang="en">
<head>
<meta charset="utf-8">
<title>Dr Clara Hollis – Clinical Psychologist</title>
<link href="https://fonts.googleapis.com/css2?family=Lora:wght@400;500;600;700&family=PT+Serif:ital,wght@0,400;0,700;1,400&display=swap" rel="stylesheet">
<style>
:root{
  --purple:#9b2a8f;
  --orange:#e0661c;
  --navy:#141936;
  --navy-deep:#1f2548;
  --ink:#2b2b35;
  --muted:#7a7a86;
  --line:#e6e6ea;
  --light:#f4f4f6;
  --teal:#1d8fb0;
  --white:#fff;
}
*{box-sizing:border-box;margin:0;padding:0}
html,body{width:1200px;height:5215px;overflow:hidden}
body{font-family:"PT Serif",serif;color:var(--ink);background:var(--white);position:relative}
.abs{position:absolute}
h1,h2,h3,h4,.head{font-family:"Lora",serif}
.label{font-size:11px;font-weight:700;color:var(--orange);letter-spacing:.5px;text-transform:uppercase;white-space:nowrap}
.center{text-align:center;left:0;right:0}
.body-text{font-size:13px;line-height:25px;color:var(--muted)}
.section-title{font-size:34px;font-weight:600;color:var(--purple)}
/* header */
.header{top:0;left:0;width:1200px;height:125px;background:var(--white)}
.contact-chip{display:flex;align-items:center;gap:10px;font-size:11px;line-height:14px}
.contact-chip b{font-weight:700;color:var(--ink)}
.contact-chip span{color:var(--muted)}
.chip-icon{width:30px;height:30px;border-radius:50%;background:var(--purple);display:flex;align-items:center;justify-content:center}
.brand{font-family:"Lora",serif;font-size:20px;font-weight:500;color:var(--purple);display:flex;align-items:center;gap:8px;letter-spacing:.5px;white-space:nowrap}
.brand-dot{width:22px;height:22px;border-radius:50%;background:var(--purple)}
.btn-appoint{background:var(--purple);color:#fff;font-size:11px;font-weight:700;border-radius:20px;width:182px;height:40px;display:flex;align-items:center;justify-content:center;text-transform:uppercase}
.nav{top:88px;left:0;width:1200px;font-size:12px;color:var(--ink)}
.nav a{position:absolute;text-decoration:none;color:inherit;white-space:nowrap}
/* hero */
.hero{top:125px;left:0;width:1200px;height:760px;background:linear-gradient(100deg,#3b3532 0%,#5a524d 45%,#7a736d 75%,#5f5954 100%)}
.hero-shade{inset:0;background:linear-gradient(90deg,rgba(20,16,14,.55),rgba(20,16,14,.1))}
.hero .kicker{top:240px;left:80px;color:#fff;font-size:22px;letter-spacing:3px;font-family:"Lora",serif}
.hero h1{top:282px;left:78px;color:#fff;font-size:48px;font-weight:600;white-space:nowrap}
.hero .rule{top:369px;left:80px;width:725px;height:1px;background:rgba(255,255,255,.7)}
.hero p{top:403px;left:82px;width:640px;color:#fff;font-size:15px;font-weight:700;line-height:25px}
.pill{height:38px;border-radius:20px;display:flex;align-items:center;justify-content:center;font-size:14px;font-weight:700}
/* features */
.feature{top:803px;width:320px;height:282px;background:#fff;border-radius:6px;box-shadow:0 6px 20px rgba(0,0,0,.12);text-align:center}
.feature svg{margin-top:32px}
.feature h3{font-size:19px;font-weight:500;color:var(--purple);margin-top:18px}
.feature p{font-size:13px;line-height:26px;color:var(--muted);margin:14px 40px 0}
/* about */
.about h2{font-size:34px;line-height:54px;color:var(--purple);font-weight:600}
.btn-orange{background:var(--orange);color:#fff;font-size:15px;font-weight:700;display:flex;align-items:center;justify-content:center;gap:10px;border-radius:3px}
.photo{border-radius:6px}
/* services */
.services{top:1663px;left:0;width:1200px;height:655px;background:var(--light)}
.service-card{top:260px;width:320px;height:287px;border-radius:6px}
.service-tag{top:520px;width:200px;height:54px;background:#fff;border-radius:4px;box-shadow:0 4px 12px rgba(0,0,0,.1);font-size:15px;font-weight:700;color:var(--purple);display:flex;align-items:center;justify-content:center;white-space:nowrap}
/* banner */
.banner{top:2318px;left:0;width:1200px;height:307px;background:linear-gradient(90deg,#a23593,#b44ca6 50%,#a23593)}
.banner h2{top:110px;color:#fff;font-size:34px;font-weight:500;line-height:43px;text-align:center}
.banner h2 em{font-style:normal;color:var(--orange)}
.contact-pill{top:2593px;left:350px;width:502px;height:57px;background:#fff;box-shadow:0 4px 14px rgba(0,0,0,.12);display:flex;align-items:center;justify-content:space-around;font-size:17px;padding:0 20px;white-space:nowrap}
/* testimonials */
.review{top:2893px;width:322px;height:262px;background:#fff;box-shadow:0 4px 16px rgba(0,0,0,.1);text-align:center}
.avatar{width:68px;height:68px;border-radius:50%;border:3px solid #fff;box-shadow:0 2px 8px rgba(0,0,0,.15)}
.stars{margin-top:64px;color:var(--orange);font-size:18px;letter-spacing:8px}
.review p{font-size:13px;line-height:25px;color:var(--muted);margin:10px 50px 0}
.quote{width:70px;height:70px;border-radius:50%;background:var(--purple);display:flex;justify-content:center;padding-top:12px;color:#fff;font-family:"Lora",serif;font-size:34px;font-weight:700;line-height:24px}
.reviewer{font-size:17px;font-weight:600;color:var(--ink);text-align:center;width:322px;font-family:"Lora",serif}
.country{font-size:12px;color:var(--muted);text-align:center;width:322px}
/* fees & information */
.why{top:3297px;left:0;width:1200px;height:600px;background:linear-gradient(90deg,#dde1e4 0%,#c9cbcb 45%,#8c6b55 65%,#5a4a3e 85%,#3d3730 100%)}
.why-card{top:63px;left:90px;width:510px;height:468px;background:#fff;border-radius:8px;box-shadow:0 6px 22px rgba(0,0,0,.12)}
.why-item{left:50px;display:flex;gap:24px}
.why-item h4{font-size:12px;font-weight:700;color:var(--purple);margin-bottom:6px}
.why-item p{font-size:12.5px;line-height:25px;color:var(--muted);white-space:nowrap}
/* form */
.form-card{top:4112px;left:140px;width:912px;height:476px;background:#fff;border-radius:14px;box-shadow:0 6px 26px rgba(0,0,0,.1)}
.field{border:2px solid var(--teal);border-radius:22px;height:44px}
.field.active{background:#d9eef5}
.field .f-label{position:absolute;top:-10px;left:30px;background:#fff;padding:0 6px;font-size:12px;font-weight:700;color:var(--ink)}
.field .f-hint{position:absolute;top:14px;left:32px;font-size:12px;font-style:italic;color:var(--muted)}
.round-soc{width:30px;height:30px;border-radius:50%;border:2px solid var(--teal)}
.btn-submit{background:var(--orange);color:#fff;border-radius:22px;width:142px;height:42px;font-size:13px;font-weight:700;display:flex;align-items:center;justify-content:space-between;padding:0 8px 0 20px}
.btn-submit i{width:28px;height:28px;border-radius:50%;background:#fff;display:flex;align-items:center;justify-content:center}
/* footer */
.footer{top:4655px;left:0;width:1200px;height:495px;background:var(--navy)}
.soc-sq{width:36px;height:36px;border-radius:3px}
.foot-info{display:flex;align-items:center;gap:14px;color:#fff;font-size:15px;white-space:nowrap}
.foot-info small{display:block;font-size:14px;color:#c9cbe0}
.foot-info b{font-weight:700}
.subfooter{top:5150px;left:0;width:1200px;height:65px;background:var(--navy-deep);color:#fff;font-size:12px;font-weight:700}
.subfooter span{position:absolute;top:24px}
</style>
</head>
<body>

<header class="abs header">
  <div class="abs contact-chip" style="top:18px;left:122px">
    <div class="chip-icon"><svg width="14" height="14" viewBox="0 0 24 24" fill="#fff"><path d="M6.6 10.8a15 15 0 0 0 6.6 6.6l2.2-2.2c.3-.3.7-.4 1-.2 1.1.4 2.3.6 3.6.6.6 0 1 .4 1 1V20c0 .6-.4 1-1 1A17 17 0 0 1 3 4c0-.6.4-1 1-1h3.5c.6 0 1 .4 1 1 0 1.3.2 2.5.6 3.6.1.3 0 .7-.2 1z"/></svg></div>
    <div><b>Call Us</b><br><span>(02) 5550 1842</span></div>
  </div>
  <div class="abs contact-chip" style="top:18px;left:280px">
    <div class="chip-icon"><svg width="14" height="14" viewBox="0 0 24 24"><rect x="3" y="5" width="18" height="14" fill="#fff"/><path d="M3 6l9 6 9-6" fill="none" stroke="var(--purple)" stroke-width="2"/></svg></div>
    <div><b>Email:</b><br><span>hello@hollispsych.au</span></div>
  </div>
  <div class="abs brand" style="top:52px;left:495px"><span class="brand-dot"></span>Dr Clara Hollis</div>
  <div class="abs" style="top:71px;left:680px;width:380px;height:1px;background:var(--line)"></div>
  <div class="abs btn-appoint" style="top:14px;left:880px">Make Appointment</div>
  <nav class="abs nav">
    <a style="left:124px">Home</a><a style="left:236px">About Us</a><a style="left:387px">Services</a>
    <a style="left:690px">Fees &amp; Information</a><a style="left:832px">Reviews</a><a style="left:956px">Contact Us</a>
  </nav>
</header>

<section class="abs hero" role="img" aria-label="Photo of a smiling mother and father with their child in a counselling session">
  <div class="abs hero-shade"></div>
  <div class="abs kicker">CHILD PSYCHOLOGIST</div>
  <h1 class="abs">Catalyst for Transformation</h1>
  <div class="abs rule"></div>
  <p class="abs">Lorem ipsum dolor sit amet, consectetur adipiscing elit et dolore conser tempor incididunt ut labore et dolore magna</p>
  <div class="abs pill" style="top:490px;left:82px;width:146px;background:var(--orange);color:#fff">LEARN MORE</div>
  <div class="abs pill" style="top:490px;left:240px;width:212px;background:#fff;color:var(--ink)">MAKE APPOINTMENT</div>
</section>

<div class="abs feature" style="left:90px">
  <svg width="64" height="56" viewBox="0 0 64 56"><circle cx="24" cy="22" r="20" fill="#fbe3d6"/><path d="M22 46h26M30 44l8-22 6 4-8 18M36 20l4-6" fill="none" stroke="var(--orange)" stroke-width="2.5"/></svg>
  <h3>Expertise</h3>
  <p>Lorem ipsum dolor sit amet, consect adipiscing elit, sed do eiusmod tempor incididunt ut labore et dolore</p>
</div>
<div class="abs feature" style="left:442px">
  <svg width="64" height="56" viewBox="0 0 64 56"><circle cx="24" cy="22" r="20" fill="#fbe3d6"/><circle cx="36" cy="30" r="16" fill="none" stroke="var(--orange)" stroke-width="2.5"/><path d="M36 30l6-8" stroke="var(--orange)" stroke-width="2.5"/></svg>
  <h3>Professional</h3>
  <p>Lorem ipsum dolor sit amet, consect adipiscing elit, sed do eiusmod tempor incididunt ut labore et dolore</p>
</div>
<div class="abs feature" style="left:787px">
  <svg width="64" height="56" viewBox="0 0 64 56"><circle cx="24" cy="22" r="20" fill="#fbe3d6"/><path d="M36 14l5 10 11 2-8 8 2 11-10-5-10 5 2-11-8-8 11-2z" fill="none" stroke="var(--orange)" stroke-width="2.5"/></svg>
  <h3>Experience</h3>
  <p>Lorem ipsum dolor sit amet, consect adipiscing elit, sed do eiusmod tempor incididunt ut labore et dolore</p>
</div>

<section class="about">
  <div class="abs label" style="top:1179px;left:100px">About Us <span style="margin-left:14px">–</span></div>
  <h2 class="abs" style="top:1196px;left:100px">Cultivating Confidence,<br>Igniting Change</h2>
  <p class="abs body-text" style="top:1315px;left:100px;width:420px;font-size:12px">Lorem ipsum dolor sit amet, consectetur adipiscing elit, sed do eius od tempor incididunt ut labore et dolore magna aliqua. Ut enim ad minim veniam, quis nostrud exercitation ullamco laboris nisi ut ali quip ex ea commodo consequat. Duis aute irure dolor in re prehenderit in voluptate velit esse cillum dolore eu fugiat nulla pariatur. Excepteur sint occaecat cupidatat non proident, sunt in culpa qui officia deserunt mollit anim id est laborum pariatur. Exce pteur sint occaecat cupidatat non proident, sunt in culpa qui</p>
  <div class="abs btn-orange" style="top:1545px;left:100px;width:155px;height:46px">Learn More
    <svg width="18" height="14" viewBox="0 0 18 14"><path d="M1 7h15M10 1l6 6-6 6" fill="none" stroke="#fff" stroke-width="2"/></svg></div>
  <div class="abs photo" style="top:1183px;left:607px;width:498px;height:407px;background:linear-gradient(120deg,#d7dde0,#bfc5c4 50%,#8a8f91)" role="img" aria-label="Photo of a psychologist with clipboard talking with a client"></div>
  <svg class="abs" style="top:1282px;left:530px" width="140" height="170" viewBox="0 0 140 170"><path d="M75 5a80 80 0 0 0 0 160" fill="none" stroke="#bbb" stroke-width="1.5" stroke-dasharray="4 4"/><path d="M80 30a55 55 0 0 0 0 110" fill="none" stroke="#bbb" stroke-width="1.5" stroke-dasharray="3 3"/><circle cx="83" cy="88" r="32" fill="#fff"/><circle cx="83" cy="88" r="10" fill="var(--purple)"/></svg>
</section>

<section class="abs services">
  <div class="abs label center" style="top:80px;text-align:center">–&nbsp;&nbsp; Our Services &nbsp;&nbsp;–</div>
  <h2 class="abs section-title center" style="top:100px;text-align:center">Our Services</h2>
  <p class="abs body-text" style="top:165px;left:300px;width:600px;text-align:center">Lorem ipsum dolor sit amet, consectetur adipiscing elit, sed do eiusod tempor incididunt ut la bore et dolore magna aliqua. Ut enim ad minim veniam, quis nostrud exercitation</p>
  <div class="abs service-card" style="left:93px;background:linear-gradient(120deg,#d8dcdc,#a8aeae)" role="img" aria-label="Photo of family therapy session"></div>
  <div class="abs service-card" style="left:442px;background:linear-gradient(120deg,#e3e3e1,#9a9c9c)" role="img" aria-label="Photo of hands writing on a clipboard next to a tablet"></div>
  <div class="abs service-card" style="left:788px;background:linear-gradient(120deg,#c9c9c6,#6e7378)" role="img" aria-label="Photo of a thoughtful man in a counselling session"></div>
  <div class="abs service-tag" style="left:152px">Family Therapy</div>
  <div class="abs service-tag" style="left:502px">Behavioral Intervention</div>
  <div class="abs service-tag" style="left:842px">Habit Formation</div>
</section>

<section class="abs banner" role="img" aria-label="Soft purple photo backdrop of comforting hands">
  <h2 class="abs center">We are available <em>24/7</em> to attend to your<br>Child Psychology needs</h2>
</section>
<div class="abs contact-pill"><span>+ (02) 5550 1842</span><span>[or]</span><span>care@hollispsych.au</span></div>

<div class="abs label center" style="top:2686px;text-align:center">–&nbsp;&nbsp; Testimonials &nbsp;&nbsp;–</div>
<h2 class="abs section-title center" style="top:2703px;text-align:center">Client Reviews</h2>
<p class="abs body-text" style="top:2768px;left:300px;width:600px;text-align:center">Lorem ipsum dolor sit amet, consectetur adipiscing elit, sed do eiusod tempor incididunt ut la bore et dolore magna aliqua. Ut enim ad minim veniam, quis nostrud exercitation</p>

<div class="abs review" style="left:92px"><div class="stars">★★★★★</div><p>Lorem ipsum dolor sit amet, consectetur adipiscing elit, sed do eiusmod tempor incididunt ut labore et dolore</p></div>
<div class="abs review" style="left:442px"><div class="stars">★★★★★</div><p>Lorem ipsum dolor sit amet, consectetur adipiscing elit, sed do eiusmod tempor incididunt ut labore et dolore</p></div>
<div class="abs review" style="left:792px"><div class="stars">★★★★★</div><p>Lorem ipsum dolor sit amet, consectetur adipiscing elit, sed do eiusmod tempor incididunt ut labore et dolore</p></div>
<div class="abs avatar" style="top:2860px;left:219px;background:#c9a88c" role="img" aria-label="Client portrait"></div>
<div class="abs avatar" style="top:2860px;left:569px;background:#e3b8b0" role="img" aria-label="Client portrait"></div>
<div class="abs avatar" style="top:2860px;left:919px;background:#e7e4e6" role="img" aria-label="Client portrait"></div>
<div class="abs quote" style="top:3120px;left:218px">“</div>
<div class="abs quote" style="top:3120px;left:568px">“</div>
<div class="abs quote" style="top:3120px;left:918px">“</div>
<div class="abs reviewer" style="top:3190px;left:92px">Ruben Marsh</div>
<div class="abs reviewer" style="top:3190px;left:442px">Ruben Marsh</div>
<div class="abs reviewer" style="top:3190px;left:792px">Ruben Marsh</div>
<div class="abs country" style="top:3220px;left:92px">Country</div>
<div class="abs country" style="top:3220px;left:442px">Country</div>
<div class="abs country" style="top:3220px;left:792px">Country</div>

<section class="abs why" role="img" aria-label="Photo of a smiling young woman with clasped hands in a counselling session">
  <div class="abs why-card">
    <div class="abs label" style="top:58px;left:50px">Fees &amp; Information <span style="margin-left:14px">–</span></div>
    <h2 class="abs" style="top:76px;left:50px;font-size:34px;color:var(--purple);font-weight:600;white-space:nowrap">Empower. Transform.</h2>
    <div class="abs why-item" style="top:150px">
      <svg width="32" height="32" viewBox="0 0 32 32"><path d="M4 28h24M10 26l8-18 6 4-8 14M18 8l3-5" fill="none" stroke="var(--orange)" stroke-width="2"/></svg>
      <div><h4>Clear Session Fees</h4><p>Lorem ipsum dolor sit amet, consectetur adipiscing elit,<br>od tempor incididunt ut labore et dolore magna</p></div>
    </div>
    <div class="abs why-item" style="top:243px">
      <svg width="32" height="32" viewBox="0 0 32 32"><path d="M16 3l4 8 9 1-7 6 2 9-8-4-8 4 2-9-7-6 9-1z" fill="none" stroke="var(--orange)" stroke-width="2"/></svg>
      <div><h4>Medicare Rebates</h4><p>Lorem ipsum dolor sit amet, consectetur adipiscing elit,<br>od tempor incididunt ut labore et dolore magna</p></div>
    </div>
    <div class="abs why-item" style="top:336px">
      <svg width="32" height="32" viewBox="0 0 32 32"><circle cx="16" cy="17" r="12" fill="none" stroke="var(--orange)" stroke-width="2"/><path d="M16 17l5-6" stroke="var(--orange)" stroke-width="2"/></svg>
      <div><h4>Flexible Booking</h4><p>Lorem ipsum dolor sit amet, consectetur adipiscing elit,<br>od tempor incididunt ut labore et dolore magna</p></div>
    </div>
  </div>
</section>

<div class="abs label" style="top:3946px;left:0;width:1200px;text-align:center">–&nbsp;&nbsp; Our Form &nbsp;&nbsp;–</div>
<h2 class="abs section-title" style="top:3963px;left:0;width:1200px;text-align:center">Get in touch with us</h2>
<p class="abs body-text" style="top:4030px;left:300px;width:600px;text-align:center">Lorem ipsum dolor sit amet, consectetur adipiscing elit, sed do eiusod tempor incididunt ut la bore et dolore magna aliqua. Ut enim ad minim veniam, quis nostrud exercitation</p>
<form class="abs form-card">
  <div class="abs field active" style="top:62px;left:52px;width:394px"><span class="f-label">First Name</span><span class="f-hint">Type Name</span></div>
  <div class="abs field" style="top:62px;left:465px;width:394px"><span class="f-label">Last Name</span><span class="f-hint">Type Name</span></div>
  <div class="abs field" style="top:136px;left:52px;width:394px"><span class="f-label">Telephone</span><span class="f-hint">02 5550 0000</span></div>
  <div class="abs field" style="top:136px;left:465px;width:394px"><span class="f-label">Your Email</span><span class="f-hint">name@example.au</span></div>
  <div class="abs field" style="top:210px;left:52px;width:807px;height:150px;border-radius:14px"><span class="f-label">Your Message</span><span class="f-hint">Type Message</span></div>
  <div class="abs round-soc" style="top:406px;left:66px"></div>
  <div class="abs round-soc" style="top:406px;left:104px"></div>
  <div class="abs round-soc" style="top:406px;left:142px"></div>
  <div class="abs round-soc" style="top:406px;left:180px"></div>
  <div class="abs btn-submit" style="top:400px;left:703px">Submit <i><svg width="12" height="12" viewBox="0 0 12 12"><path d="M4 2l4 4-4 4" fill="none" stroke="var(--orange)" stroke-width="2"/></svg></i></div>
</form>

<footer class="abs footer">
  <div class="abs soc-sq" style="top:103px;left:85px;background:#3b5998"></div>
  <div class="abs soc-sq" style="top:103px;left:135px;background:#2a6db0"></div>
  <div class="abs soc-sq" style="top:103px;left:185px;background:#1da1f2"></div>
  <div class="abs soc-sq" style="top:103px;left:235px;background:#e0252b"></div>
  <div class="abs brand" style="top:104px;left:450px;color:#fff;font-size:24px"><span class="brand-dot" style="background:#fff;width:26px;height:26px"></span>Dr Clara Hollis</div>
  <div class="abs" style="top:114px;left:988px;color:#fff;font-size:13px;font-weight:700">Go to top</div>
  <div class="abs" style="top:100px;left:1070px;width:44px;height:44px;background:var(--orange);display:flex;align-items:center;justify-content:center"><svg width="18" height="12" viewBox="0 0 18 12"><path d="M2 10l7-7 7 7" fill="none" stroke="#fff" stroke-width="2.5"/></svg></div>
  <div class="abs" style="top:177px;left:82px;width:1033px;height:1px;background:#5b6080"></div>
  <h2 class="abs" style="top:243px;left:0;width:1200px;text-align:center;color:#fff;font-size:25px;font-weight:600">Elevate Your Life, Elevate Your Mind</h2>
  <p class="abs" style="top:295px;left:300px;width:600px;text-align:center;color:#fff;font-size:15px;line-height:24px">Lorem ipsum dolor sit amet, consectetur adipiscing elit, sed do eiusod tempor incididunt ut labore et dolore magna aliqua.</p>
  <div class="abs foot-info" style="top:378px;left:232px">
    <svg width="38" height="46" viewBox="0 0 38 46"><rect x="4" y="2" width="22" height="42" rx="3" fill="none" stroke="var(--orange)" stroke-width="2"/><path d="M30 16a8 8 0 0 1 0 14M34 12a13 13 0 0 1 0 22" fill="none" stroke="var(--orange)" stroke-width="2"/></svg>
    <div><small>Call Us</small><b>+61 2 5550 1842</b></div>
  </div>
  <div class="abs" style="top:378px;left:455px;width:1px;height:46px;background:#5b6080"></div>
  <div class="abs foot-info" style="top:378px;left:475px">
    <svg width="46" height="46" viewBox="0 0 46 46"><rect x="3" y="12" width="40" height="30" fill="none" stroke="var(--orange)" stroke-width="2"/><path d="M3 12l20 16 20-16" fill="none" stroke="var(--orange)" stroke-width="2"/></svg>
    <div><small>Mail Us</small><b>care@hollispsych.au</b></div>
  </div>
  <div class="abs" style="top:378px;left:726px;width:1px;height:46px;background:#5b6080"></div>
  <div class="abs foot-info" style="top:378px;left:758px">
    <svg width="46" height="46" viewBox="0 0 46 46"><path d="M23 40s-12-13-12-22a12 12 0 0 1 24 0c0 9-12 22-12 22z" fill="none" stroke="var(--orange)" stroke-width="2"/><circle cx="23" cy="18" r="4" fill="none" stroke="var(--orange)" stroke-width="2"/><path d="M4 44h38" stroke="var(--orange)" stroke-width="2"/></svg>
    <div><small>Location</small><b>14 Wattle Grove Rd</b></div>
  </div>
</footer>
<div class="abs subfooter">
  <span style="left:85px">Dr Clara Hollis</span>
  <span style="left:690px">Privacy</span>
  <span style="left:834px">Cookies Policy</span>
  <span style="left:1012px">Site Map</span>
</div>

</body>
</html>
```